Brantley & Co Flyer (tri-fold) Accounting Firm

We are an accounting firm that provides loan broking services. We would like the brochure to look sophisticated but not too formal.

We would like to add some background colour to the flyer/brochure (attached in word and PDF version) in the following green (Hex Colour #94c947) in different styles/patterns etc.

Guidelines:

• We envisage that the green would cover approximately 30% of the background

• Do not change any of the content

• Change fonts as required

• The wording, titles/headings and background can be a combination of the green colour #94c947, black and white.

• We are happy to use multiple shadings of the green colour above to give contrast and depth

• We would like a 3-5mm bleed around the edges.

• Please remove black page break lines are to disappear (not sure how to remove on word document).

• Please stretch all images to the edge of the bleed (except for KLVN, Ledgerline Planner, Homeward Select and EasyNest 480 logos).

• Please insert different icons for phone, fax and email, e.g. an image of a telephone next to our number instead of the symbol “P”.

We have included a copy of a business card as an example of our existing style we wish to retain in the brochure.

Please provide appropriate file types to enable publishing of brochures.

Target Market(s)

Business owners and individuals requiring accounting and services, people requiring loans/refinance, superannuation retirees

Industry/Entity Type

Accounting

Font styles to use
Other font styles liked:
• Refer to business card font

Colors
abd037

Requirements
Must have
• Must use our Brantley & Co logo green with black text (as in the attached brochure).
Nice to have
• The design concept does not need to necessarily include the KLVN, Ledgerline Planner, Homeward Select and EasyNest 480 logos, this may create a simpler cleaner look. I'd like to look at the brochure design with and without those additional logos for comparison purposes.

```html
<!DOCTYPE html>
<html lang="en">
<head>
<meta charset="utf-8">
<title>Brantley &amp; Co Tri-fold Brochure</title>
<link rel="stylesheet" href="https://fonts.googleapis.com/css2?family=Cinzel:wght@400;600&family=Questrial&family=Montserrat:wght@600;800&display=swap">
<style>
  :root {
    --green: #94c947;
    --green-deep: #7fb236;
    --charcoal: #3a3a3a;
    --charcoal-dark: #2a2a2a;
    --ink: #1e1e1e;
    --white: #ffffff;
    --page: #e9e9e6;
    --rule: #94c947;
  }
  * { box-sizing: border-box; margin: 0; padding: 0; }
  html, body { width: 1200px; height: 777px; overflow: hidden; }
  body {
    background: var(--page);
    font-family: "Questrial", "Century Gothic", sans-serif;
    color: var(--ink);
    display: flex; align-items: center; justify-content: center;
  }
  .brochure {
    width: 1110px; height: 730px;
    display: flex;
    background: var(--white);
    box-shadow: 0 4px 18px rgba(0,0,0,.18);
  }
  .panel { width: 370px; height: 100%; display: flex; flex-direction: column; position: relative; }
  .panel + .panel { border-left: 1px solid #e4e4e4; }

  .panel-head {
    background: var(--charcoal);
    height: 62px;
    border-bottom: 5px solid var(--green);
    display: flex; align-items: center; justify-content: center;
    font-family: "Cinzel", serif; font-weight: 600;
    color: var(--green); font-size: 19px; letter-spacing: 1px;
    text-align: center; line-height: 1.05;
  }

  /* Tax panel */
  .intro { padding: 18px 28px 8px; font-size: 13.5px; text-align: center; line-height: 1.3; }
  .entities { font-size: 12.5px; text-align: center; line-height: 1.3; margin-bottom: 8px; }
  .bar-label {
    margin: 0 28px; background: var(--green);
    font-family: "Montserrat", sans-serif; font-weight: 800;
    font-size: 14px; text-align: center; padding: 4px 0; color: var(--ink);
  }
  .rule-list { list-style: none; margin: 0 48px; }
  .rule-list li {
    text-align: center; font-size: 13px; padding: 4px 0 3px;
    border-bottom: 1.5px solid var(--rule);
  }
  .business-box { margin: 18px 28px 0; background: var(--green); padding-bottom: 12px; }
  .business-box .box-title {
    background: var(--charcoal); color: var(--green);
    font-family: "Montserrat", sans-serif; font-weight: 800;
    font-size: 14px; text-align: center; padding: 7px 0;
  }
  .business-box p { font-size: 13.5px; text-align: center; padding: 8px 16px 4px; line-height: 1.25; }
  .business-box .rule-list { margin: 0 22px; }
  .business-box .rule-list li { border-bottom-color: var(--charcoal); font-size: 13.5px; padding: 5px 0 4px; }

  .partner {
    margin-top: auto; height: 88px;
    display: flex; flex-direction: column; align-items: center; justify-content: center; gap: 2px;
  }
  .partner-name {
    display: flex; align-items: center; gap: 8px;
    font-family: "Montserrat", sans-serif; font-weight: 800; font-size: 20px; color: var(--charcoal);
  }
  .partner-name .dot { width: 20px; height: 20px; border-radius: 50%; background: var(--green); }
  .partner-tag { font-size: 9px; color: #555; }

  /* Mortgage panel */
  .photo { background: linear-gradient(135deg, #d8d8d8, #6f6f6f 55%, #2f2f2f); }
  .photo-mortgage { height: 205px; }
  .loan-block { background: var(--green); padding: 16px 28px 0; flex: 1; }
  .loan-block p { font-size: 13.5px; line-height: 1.28; }
  .loan-list { list-style: none; margin: 12px 0 0 10px; }
  .loan-list li { font-size: 14px; padding: 7px 0 5px; border-bottom: 1.5px solid var(--charcoal); }
  .call-out {
    margin: 22px 6px 20px; background: var(--charcoal);
    color: var(--green); font-family: "Montserrat", sans-serif; font-weight: 800;
    text-align: center; padding: 12px 10px; line-height: 1.05;
  }
  .call-out .small { font-size: 17px; display: block; }
  .call-out .large { font-size: 26px; display: block; }
  .panel-mortgage .partner { height: 100px; }

  /* Super panel */
  .super-text { padding: 16px 26px 10px; font-size: 13px; line-height: 1.3; }
  .super-text p + p { margin-top: 10px; }
  .photo-super { height: 190px; background: linear-gradient(160deg, #cfcfcf, #8a8a8a 50%, #444); }
  .super-list { list-style: none; margin: 14px 40px 0; }
  .super-list li { font-size: 13.5px; padding: 4px 0 3px; border-bottom: 1.5px solid var(--rule); }
  .consult {
    margin: 10px 26px 0; background: var(--green);
    font-family: "Montserrat", sans-serif; font-weight: 800; font-size: 15px;
    color: var(--charcoal); text-align: center; padding: 8px 10px; line-height: 1.15;
  }
</style>
</head>
<body>
<main class="brochure">

  <section class="panel panel-tax">
    <h2 class="panel-head">Tax Services</h2>
    <p class="intro">We prepare tax returns ranging from the simplest individual return to the most complex business.</p>
    <p class="entities">INDIVIDUALS, PARTNERSHIPS,<br>COMPANIES, TRUSTS AND SMSF'S</p>
    <div class="bar-label">INCLUDING:</div>
    <ul class="rule-list">
      <li>Rental properties</li>
      <li>Capital Gains Tax</li>
      <li>Share Portfolios</li>
      <li>GST, BAS and IAS</li>
      <li>Deceased estates</li>
      <li>Tax Planning</li>
      <li>ATO communications</li>
    </ul>
    <div class="business-box">
      <div class="box-title">OWN YOUR OWN BUSINESS?</div>
      <p>We understand running a business is hard work. Let us work with you to help improve your business performance.</p>
      <ul class="rule-list">
        <li>New business start up</li>
        <li>Purchase and sale of business</li>
        <li>Asset protection</li>
        <li>Succession planning</li>
        <li>Purchase and sale of property</li>
        <li>Budgeting and benchmarking</li>
        <li>Cloud accounting software</li>
      </ul>
    </div>
    <div class="partner">
      <div class="partner-name"><span class="dot"></span>Ledgerline Planner</div>
      <div class="partner-tag">Simple bookkeeping for every business</div>
    </div>
  </section>

  <section class="panel panel-mortgage">
    <h2 class="panel-head">Have you reviewed<br>your loan lately?</h2>
    <div class="photo photo-mortgage" role="img" aria-label="Businessman's hand pressing a touchscreen button labelled Mortgage Interest"></div>
    <div class="loan-block">
      <p>We provide our clients with a FREE annual review of their existing commercial and residential loan portfolio and can assist our clients in obtaining new loans.</p>
      <ul class="loan-list">
        <li>Free annual loan portfolio review</li>
        <li>Selection of 25 residential lenders</li>
        <li>Selection of 8 commercial lenders</li>
        <li>Secure competitive rates available in the market</li>
      </ul>
      <div class="call-out">
        <span class="small">SIMPLY GIVE US A CALL</span>
        <span class="large">AND WE WILL</span>
        <span class="small">HANDLE THE REST.</span>
      </div>
    </div>
    <div class="partner">
      <div class="partner-name"><span class="dot"></span>Homeward Select</div>
    </div>
  </section>

  <section class="panel panel-super">
    <h2 class="panel-head">Take control of your Super</h2>
    <div class="super-text">
      <p>SMSF's are a fast growing vehicle for investment, accounting for approximately one third of all superannuation assets with more than 6,500 funds being setup per quarter.</p>
      <p>The SMSF structure enables members to have the flexibility to CONTROL their investment strategy to suit their personal circumstances.</p>
    </div>
    <div class="photo photo-super" role="img" aria-label="Smiling retired shop owner standing with arms folded in front of his store"></div>
    <ul class="super-list">
      <li>SMSF Establishment/Rollover</li>
      <li>Compliance obligations</li>
      <li>Consultancy and strategic advice</li>
      <li>Retirement strategies</li>
      <li>Estate planning</li>
    </ul>
    <div class="consult">SPEAK TO ONE OF OUR CONSULTANTS ABOUT OUR SMSF SERVICES.</div>
    <div class="partner">
      <div class="partner-name"><span class="dot"></span>EasyNest 480</div>
    </div>
  </section>

</main>
</body>
</html>
```